Banner ads for VL that work with same theme as below banners

Love the banner ads below. Need more with attached photos. But use the same wording, font as in below banner ads. Should be VL size 1200/627 so I can use for Trovique and VL. Looking for great ads to use as VL ads. We do lots of ads so it will be worth your time to enter this contest you will be rewarded with a ton of work. Need several banner ads that work together. So maybe 1 of the dresses, 1 of the sweater, 1 of the leggings, 1 of the jacket

Target Market(s)

Women 24-45

Industry/Entity Type

Fashion

Requirements
Must have
• Banner ads that work for VL and Trovique
Nice to have
• Several options to choose from
Should not have
• not sure

```html
<!DOCTYPE html>
<html lang="en">
<head>
<meta charset="UTF-8">
<title>Winter Wear Collection Banner</title>
<link href="https://fonts.googleapis.com/css2?family=Playfair+Display:ital,wght@1,700&family=Libre+Baskerville:wght@700&display=swap" rel="stylesheet">
<style>
  :root {
    --paper: #f7f8fa;
    --blue-main: #1177f0;
    --blue-light: #2a93f7;
    --blue-deep: #0a5fe0;
    --blue-faint: #e4ebf7;
    --ink: #ffffff;
    --ghost: rgba(10, 40, 110, 0.35);
    --button: #1b1a1c;
    --jacket-navy: #1d3a66;
    --jacket-black: #1f2226;
    --knit-grey: #a7a7a7;
  }
  * { margin: 0; padding: 0; box-sizing: border-box; }
  html, body { width: 1200px; height: 627px; overflow: hidden; background: var(--paper); }
  .banner { position: relative; width: 1200px; height: 627px; overflow: hidden; background: var(--paper); }
  .backdrop { position: absolute; inset: 0; }
  .headline-watermark {
    position: absolute; left: 160px; top: -22px;
    font-family: "Playfair Display", serif; font-style: italic; font-weight: 700;
    font-size: 132px; letter-spacing: 10px; color: var(--blue-faint); white-space: nowrap;
  }
  .model-photo { position: absolute; }
  .model-photo--navy {
    left: 22px; top: 0; width: 270px; height: 590px;
    background: linear-gradient(180deg, #c9a88a 0%, #b38f70 14%, var(--jacket-navy) 22%, #22406e 70%, var(--knit-grey) 76%, #9a9a9a 86%, #141414 92%);
    border-radius: 120px 120px 10px 10px;
  }
  .model-photo--black {
    left: 292px; top: 88px; width: 290px; height: 457px;
    background: linear-gradient(180deg, #6d6d6d 0%, #c6b7a8 26%, var(--jacket-black) 38%, #25282c 76%, var(--knit-grey) 82%, #999 92%, #151515 96%);
    border-radius: 110px 110px 0 0;
  }
  .copy { position: absolute; left: 625px; top: 238px; }
  .copy__script {
    font-family: "Playfair Display", serif; font-style: italic; font-weight: 700;
    font-size: 46px; letter-spacing: 3px; color: var(--ink); line-height: 1;
  }
  .copy__title-wrap { position: relative; margin-top: 14px; height: 62px; }
  .copy__title-ghost {
    position: absolute; left: 8px; top: -12px;
    font-family: "Libre Baskerville", serif; font-weight: 700;
    font-size: 66px; letter-spacing: 1px; color: var(--ghost); white-space: nowrap;
  }
  .copy__title {
    position: absolute; left: -2px; top: 0;
    font-family: "Libre Baskerville", serif; font-weight: 700;
    font-size: 47px; color: var(--ink); white-space: nowrap;
  }
  .cta {
    position: absolute; left: 625px; top: 409px; width: 226px; height: 59px;
    background: var(--button); color: var(--ink);
    display: flex; align-items: center; justify-content: center;
    font-family: "Libre Baskerville", serif; font-weight: 700;
    font-size: 13px; letter-spacing: 2.5px; text-decoration: none;
  }
</style>
</head>
<body>
<div class="banner">
  <svg class="backdrop" width="1200" height="627" viewBox="0 0 1200 627" aria-hidden="true">
    <defs>
      <clipPath id="torn-band">
        <path d="M0 100 L60 96 L110 104 L180 92 L240 108 L300 98 L360 112 L420 96 L470 118 L520 104 L580 122 L640 108 L700 116 L760 96 L820 110 L880 100 L940 114 L980 96 L1010 72 L1040 90 L1100 82 L1150 96 L1200 88 L1200 600 L1160 556 L1100 548 L1040 560 L980 544 L920 556 L860 540 L800 552 L740 538 L680 550 L620 540 L560 552 L500 544 L440 556 L380 542 L320 552 L260 546 L200 560 L140 572 L80 566 L20 578 L0 574 Z"/>
      </clipPath>
    </defs>
    <g clip-path="url(#torn-band)">
      <rect width="1200" height="627" fill="var(--blue-main)"/>
      <polygon points="0,90 420,90 180,360 0,300" fill="var(--blue-light)"/>
      <polygon points="420,90 760,90 600,330" fill="var(--blue-deep)"/>
      <polygon points="760,90 1200,90 1200,260 900,200" fill="#1a86f5"/>
      <polygon points="900,200 1200,260 1200,620 1020,620" fill="var(--blue-light)"/>
      <polygon points="600,330 900,200 1020,620 700,620" fill="#0f6ee8"/>
      <polygon points="0,300 180,360 300,620 0,620" fill="#1580f2"/>
      <polygon points="180,360 600,330 700,620 300,620" fill="var(--blue-main)"/>
    </g>
  </svg>

  <div class="headline-watermark" aria-hidden="true">Winter Wear</div>

  <div class="model-photo model-photo--navy" role="img" aria-label="Model in a navy quilted puffer jacket with faux fur collar and grey knit hem"></div>
  <div class="model-photo model-photo--black" role="img" aria-label="Model in a black hooded quilted puffer jacket with faux fur trim and grey knit hem"></div>

  <div class="copy">
    <p class="copy__script">Winter Wear</p>
    <div class="copy__title-wrap">
      <span class="copy__title-ghost" aria-hidden="true">COLLECTION</span>
      <h1 class="copy__title">COLLECTION</h1>
    </div>
  </div>

  <a class="cta" href="#">SHOP THE LOOK</a>
</div>
</body>
</html>
```